Ribbon Cutting Ceremony Invitation for Solar Company

Need 8.5 x 11 Ribbon Cutting Invitation Design to be used for digital and print. The design should be professional yet creative. It should showcase the theme of a ribbon cutting with some sort of style resembling solar energy. There could also be an option to include a placeholder for a photo of the facility, but that is up to your creative direction. Thanks designers!

Words that should be on it are below:

RIBBON CUTTING CEREMONY

WE FORMALLY INVITE YOU TO THE RIBBON CUTTING EVENT FOR THE NEW SOLAR SYSTEM @ SEABRAMBLE HOTEL AND RESORT.

DATE AND TIME

Use this logo in one of the corners: https://files.plenvarq-media.net/assets/k/kd/Vexa_Energy.png - Let me know if you need it in a different version, transparent, or all white.

PLEASE ASK ME ANY QUESTIONS!!!

Target Market(s)

Business Owners and Executives

Colors

Designer to choose colors to be used in the design.

Requirements
Must have
• Professional design with ribbon cutting and solar theme.

```html
<!DOCTYPE html>
<html lang="en">
<head>
<meta charset="UTF-8">
<title>Ribbon Cutting Ceremony Invitation</title>
<link href="https://fonts.googleapis.com/css2?family=Roboto:wght@300;400;500;700;900&display=swap" rel="stylesheet">
<style>
  :root {
    --paper: #ffffff;
    --ink: #1c1c1c;
    --brand-orange: #f26a21;
    --red-deep: #e3222b;
    --red-light: #f4565b;
    --white: #ffffff;
    --sky-top: #8aa6c4;
    --sky-low: #d6dde4;
    --panel: #4f6282;
    --field: #4a5238;
  }
  * { margin: 0; padding: 0; box-sizing: border-box; }
  html, body { width: 849px; height: 1200px; overflow: hidden; background: var(--paper); }
  .invitation {
    position: relative;
    width: 849px;
    height: 1200px;
    overflow: hidden;
    background: var(--paper);
    font-family: 'Roboto', Arial, sans-serif;
  }
  .brand {
    position: absolute;
    top: 44px;
    left: 48px;
    display: flex;
    align-items: center;
    gap: 14px;
    z-index: 2;
  }
  .brand-dot {
    width: 54px;
    height: 54px;
    border-radius: 50%;
    background: var(--brand-orange);
  }
  .brand-name {
    font-size: 34px;
    font-weight: 700;
    color: var(--ink);
  }
  .event-date {
    position: absolute;
    top: 36px;
    right: 52px;
    display: flex;
    align-items: center;
    gap: 10px;
    color: var(--ink);
    z-index: 2;
  }
  .event-day { font-size: 62px; font-weight: 700; line-height: 1; }
  .event-month { font-size: 27px; font-weight: 700; line-height: 1; }
  .event-time { font-size: 23px; font-weight: 400; line-height: 1.1; }
  .facility-photo {
    position: absolute;
    top: 118px;
    left: 0;
    width: 849px;
    height: 800px;
    background: linear-gradient(180deg, var(--sky-top) 0%, var(--sky-low) 32%, var(--panel) 58%, var(--field) 100%);
  }
  .ribbon-band {
    position: absolute;
    left: 0;
    top: 600px;
    width: 849px;
    height: 600px;
  }
  .headline {
    position: absolute;
    top: 846px;
    left: 0;
    width: 100%;
    text-align: center;
    color: var(--white);
  }
  .headline-main {
    font-size: 66px;
    font-weight: 700;
    letter-spacing: 1px;
    line-height: 1.05;
  }
  .headline-sub {
    font-size: 50px;
    font-weight: 300;
    letter-spacing: 2px;
    line-height: 1.1;
  }
  .divider {
    position: absolute;
    top: 1024px;
    left: 110px;
    width: 629px;
    height: 1px;
    background: rgba(255,255,255,0.75);
  }
  .invite-text {
    position: absolute;
    top: 1068px;
    left: 104px;
    width: 641px;
    text-align: center;
    color: var(--white);
    font-size: 16px;
    font-weight: 500;
    line-height: 1.55;
    text-transform: uppercase;
  }
</style>
</head>
<body>
<main class="invitation">
  <header>
    <div class="brand">
      <span class="brand-dot"></span>
      <span class="brand-name">Vexa Energy</span>
    </div>
    <div class="event-date">
      <span class="event-day">30</span>
      <span>
        <span class="event-month">JAN</span><br>
        <span class="event-time">02 PM</span>
      </span>
    </div>
  </header>

  <div class="facility-photo" role="img" aria-label="Rows of solar panels under a cloudy blue sky on a grassy field, with a red ribbon and golden scissors"></div>

  <svg class="ribbon-band" viewBox="0 0 849 600" preserveAspectRatio="none" aria-hidden="true">
    <defs>
      <linearGradient id="bandFill" x1="0" y1="0" x2="0" y2="1">
        <stop offset="0" stop-color="var(--red-deep)"/>
        <stop offset="1" stop-color="var(--red-light)"/>
      </linearGradient>
    </defs>
    <path d="M0 80 C 180 170, 360 200, 520 150 C 660 105, 760 40, 849 0 L849 600 L0 600 Z" fill="url(#bandFill)"/>
  </svg>

  <section class="headline">
    <h1 class="headline-main">RIBBON CUTTING</h1>
    <p class="headline-sub">CEREMONY</p>
  </section>

  <div class="divider"></div>

  <p class="invite-text">We formally invite you to the ribbon cutting event for the<br>new solar system @ Seabramble Hotel and Resort.</p>
</main>
</body>
</html>
```